Etiketten für Weinflasche
Zielgruppe
HANDARBEIT
HAT SEELE.
»80 % gibt uns die Natur vor,
für die restlichen 20 % geben wir alles!«
Volker Brandhuber
Seit über 125 Jahren ist die Rotweinstadt Ingelheim Sitz unseres Familienbetriebes. Im alten Ober-Ingelheimer Schulhaus gelegen, betreiben wir das Weingut in der nunmehr 5. Generation. Unser hoher Qualitätsanspruch und Traditionsbewusstsein wird von Kennern eines guten Weines geschätzt. Zusammen mit der Natur und so schonend wie möglich bewirtschaften wir die rund 15 ha Weinberge in den besten Lagen Ingelheims.
Ganz in der Tradition Karls des Großen, der die Rotweinreben um 800 n. Chr. nach Ingelheim brachte, sind die Spät- und Frühburgunder die Spezialitäten unseres Hauses. Seit 2015 sind wir Träger des „Goldenen Traubenpokals' des Weinkulturmagazins Korkla. Das macht uns stolz und gibt uns Energie. Auch die Rieslinge und die weißen Burgundersorten stehen im Fokus und werden mit viel Gefühl zum Detail gekeltert. Den geselligen Mittelpunkt des Weinguts bildet unser über hundert Jahre alter Pavillon. Er steht symbolisch für uns als gastliche Weinfamilie und vertritt unser Weingut auch nach außen auf unseren Etiketten.
Aufgabenstellung
Ein Wein für FRANKFURTER
Wir möchten für einen führende Marktis-Gruppe in Frankfurt eine Weißwein-Sonderedition entwickeln.
Es soll ein Label sein, womit sich jeder Frankfurter identifizieren kann (Skyline gab es schon mal ist aber nicht ausgeschlossen) und dazu animiert wird die Weinflasche blind zu kaufen.
Die Rebsorte soll auf dem Vorderetikett genannt werden. Es ist ein Grauburgunder oder Grauer Burgunder. Der Wein soll ein schönes Mitbringsel oder auch für den eigenen Genuss sein. Die Flasche wird sich im mittleren Preissegment bewegen +/- 10€ im Verkauf. Zielgruppe 40-65 Jahre alt.
Es gibt drei mögliche Etikettengrößen.
Variante 1: Bestehendes Brandhuber-Etikett mit Streifen (wie in der Anlage)
Variante 2: Vorder- und Rückenetikett mit je 7cm x 7cm oder
Variante 3: Vorderetikett (9cm Breit x 6cm hoch) und Rückenetikett (7cm Breit x 6cm hoch)
Die Rückseite kann ein : gestalterisches Element vom Vorderetikett beinhalten, ist aber durch die gesetzlichen Angaben und den EAN-Code schon ziemlich ausgelastet. Es zum größten Teil um das Vorderetikett.
Die Kapsel am Flaschenhals ist weiß mit gelber Markierung und es gibt eine gelbe Kapsel mit weißer Markierung. Diese ist beiden sind fix, da der Wein schon abgefüllt ist. Es ist eine Burgunderflasche.
Ein Flaschenbild stelle ich zur Verfügung.

```html
<!DOCTYPE html>
<html lang="de">
<head>
<meta charset="utf-8">
<title>Grauer Burgunder – Vorderetikett</title>
<link rel="stylesheet" href="https://fonts.googleapis.com/css2?family=Montserrat:wght@300;400;500&display=swap">
<style>
  :root {
    --page-bg: #ffffff;
    --gold-left: #e3a11c;
    --gold-mid: #f1bf36;
    --gold-right: #db8713;
    --frame-gold: #f3cf6a;
    --accent-gold: #d89a22;
    --text-white: #ffffff;
    --text-black: #151210;
    --label-white: #ffffff;
    --skyline-light: rgba(255, 255, 255, 0.38);
    --skyline-mist: rgba(244, 241, 236, 0.92);
  }
  html, body {
    margin: 0;
    padding: 0;
    width: 1200px;
    height: 1200px;
    overflow: hidden;
    background: var(--page-bg);
  }
  .canvas {
    position: relative;
    width: 1200px;
    height: 1200px;
  }
  .label {
    position: absolute;
    left: 243px;
    top: 79px;
    width: 714px;
    height: 1042px;
    background: linear-gradient(90deg, var(--gold-left) 0%, var(--gold-mid) 50%, var(--gold-right) 100%);
    overflow: hidden;
    font-family: "Montserrat", sans-serif;
  }
  .label__white-base {
    position: absolute;
    left: 0;
    right: 0;
    top: 860px;
    bottom: 0;
    background: var(--label-white);
  }
  .label__skyline {
    position: absolute;
    left: 0;
    right: 0;
    top: 540px;
    height: 330px;
    background: linear-gradient(180deg, var(--skyline-light) 0%, var(--skyline-light) 35%, var(--skyline-mist) 80%, var(--label-white) 100%);
  }
  .label__frame {
    position: absolute;
    inset: 20px;
    border: 2px solid var(--frame-gold);
  }
  .label__mark {
    position: absolute;
    left: 327px;
    top: 92px;
    width: 56px;
    height: 56px;
    border: 3px solid var(--text-white);
    box-sizing: border-box;
  }
  .label__winery {
    position: absolute;
    left: 0;
    right: 0;
    top: 186px;
    text-align: center;
    color: var(--text-white);
    font-weight: 300;
    font-size: 19px;
    letter-spacing: 1px;
  }
  .label__variety {
    position: absolute;
    left: 0;
    right: 0;
    text-align: center;
    margin: 0;
    line-height: 1;
  }
  .label__variety--grauer {
    top: 281px;
    font-size: 127px;
    font-weight: 500;
    color: var(--text-white);
    letter-spacing: -1px;
  }
  .label__variety--burgunder {
    top: 418px;
    font-size: 78px;
    font-weight: 400;
    color: var(--text-black);
  }
  .label__style {
    position: absolute;
    left: 0;
    right: 0;
    top: 958px;
    text-align: center;
    color: var(--accent-gold);
    font-size: 30px;
    font-weight: 400;
    line-height: 1;
    letter-spacing: 14px;
    padding-left: 14px;
  }
</style>
</head>
<body>
<main class="canvas">
  <section class="label">
    <div class="label__white-base"></div>
    <div class="label__skyline" role="img" aria-label="Linienzeichnung der Frankfurter Skyline mit Mainbrücke"></div>
    <div class="label__frame"></div>
    <div class="label__mark"></div>
    <div class="label__winery">BRANDHUBER</div>
    <h1 class="label__variety label__variety--grauer">GRAUER</h1>
    <h2 class="label__variety label__variety--burgunder">BURGUNDER</h2>
    <div class="label__style">TROCKEN</div>
  </section>
</main>
</body>
</html>
```